Bref créative
Edgy modern Letterhead an B. card for jet charter company
Veltaro Corporation
Professional
Peter Haldane
Founder, Chief Pilot
246 W. Harbor Ave., Suite 2020
Long Beach, CA 90815
855.5.VELTARO
phal@veltaro-example.com
veltaro-example.com
Use: Veltaro Corporation for company name

```html
<!DOCTYPE html>
<html lang="en">
<head>
<meta charset="utf-8">
<title>Veltaro Corporation – Stationery</title>
<link href="https://fonts.googleapis.com/css2?family=Montserrat:wght@400;500&display=swap" rel="stylesheet">
<style>
:root{
  --bg:#e4e4e4;
  --paper:#ffffff;
  --ink:#111111;
  --band:#a9a9a9;
  --line:#3a3a3a;
  --font:"Montserrat",Arial,sans-serif;
}
*{margin:0;padding:0;box-sizing:border-box}
html,body{width:1200px;height:895px;overflow:hidden;background:var(--bg);font-family:var(--font)}
.canvas{position:relative;width:1200px;height:895px}
.piece{position:absolute;background:var(--paper);box-shadow:0 2px 6px rgba(0,0,0,.25);overflow:hidden}
.wordmark{font-family:var(--font);font-weight:500;color:var(--ink);letter-spacing:.5px;line-height:1}
.wordmark--light{color:var(--paper)}
.small{font-size:5px;color:var(--ink);line-height:1.5}
.small--light{color:var(--paper)}
.band{position:absolute;left:0;right:0;background:var(--band)}
.bar{position:absolute;left:0;right:0;background:var(--ink)}

/* CD */
.disc{position:absolute;left:116px;top:92px;width:118px;height:118px}

/* CD sleeve */
.sleeve{left:310px;top:48px;width:186px;height:218px}

/* folder */
.folder{left:508px;top:116px;width:622px;height:566px}
.folder__pockets{position:absolute;left:0;right:0;bottom:0;height:150px}

/* letterhead */
.letterhead{left:194px;top:290px;width:300px;height:383px}

/* business cards */
.card{width:122px;height:50px}
.card--front{left:29px;top:290px;display:flex}
.card--back{left:29px;top:387px;background:var(--ink)}
.card--right{left:864px;top:690px;width:152px;height:54px;display:flex}

/* compliment slip & envelope */
.slip{left:160px;top:690px;width:336px;height:150px}
.envelope{left:508px;top:690px;width:334px;height:150px}
</style>
</head>
<body>
<main class="canvas">

  <!-- disc -->
  <svg class="disc" viewBox="0 0 118 118" aria-label="Veltaro disc label">
    <defs><clipPath id="discClip"><circle cx="59" cy="59" r="58"/></clipPath></defs>
    <g clip-path="url(#discClip)">
      <rect width="118" height="118" fill="#ffffff"/>
      <rect y="62" width="118" height="56" fill="#111111"/>
    </g>
    <circle cx="59" cy="59" r="58" fill="none" stroke="#888" stroke-width="1"/>
    <circle cx="59" cy="59" r="12" fill="#e4e4e4" stroke="#888"/>
    <circle cx="59" cy="59" r="5" fill="#bbb"/>
    <text x="59" y="40" text-anchor="middle" font-family="Montserrat,Arial,sans-serif" font-weight="500" font-size="16" fill="#111">veltaro</text>
  </svg>

  <!-- CD sleeve -->
  <section class="piece sleeve">
    <div class="bar" style="top:0;height:30px"></div>
    <div class="wordmark" style="position:absolute;left:40px;top:62px;font-size:20px">veltaro</div>
    <div class="band" style="top:170px;height:36px"></div>
  </section>

  <!-- presentation folder -->
  <section class="piece folder">
    <div class="band" style="top:0;height:26px"></div>
    <div class="wordmark" style="position:absolute;right:70px;top:130px;font-size:40px">veltaro</div>
    <div class="wordmark" style="position:absolute;left:120px;top:312px;font-size:14px">veltaro</div>
    <p class="small" style="position:absolute;left:90px;top:334px">246 W. Harbor Ave., Suite 2020, Long Beach, CA 90815</p>
    <div class="bar" style="top:386px;height:3px"></div>
    <div class="band" style="top:389px;height:27px"></div>
    <svg class="folder__pockets" viewBox="0 0 622 150" preserveAspectRatio="none">
      <rect width="622" height="150" fill="#111"/>
      <polygon points="290,0 332,0 352,150 270,150" fill="#e4e4e4"/>
      <line x1="311" y1="0" x2="311" y2="150" stroke="#333"/>
      <rect x="440" y="40" width="90" height="50" fill="none" stroke="#2a2a2a"/>
    </svg>
  </section>

  <!-- business card front -->
  <section class="piece card card--front">
    <div style="width:50%;background:var(--band);position:relative">
      <div class="wordmark" style="position:absolute;left:6px;top:8px;font-size:9px">veltaro</div>
    </div>
    <div style="width:50%;background:var(--ink);padding:5px 4px">
      <p class="small small--light" style="font-size:4px">Peter Haldane<br>Founder, Chief Pilot<br>855.5.VELTARO<br>phal@veltaro-example.com<br>veltaro-example.com</p>
    </div>
  </section>

  <!-- business card back -->
  <section class="piece card card--back">
    <div class="wordmark wordmark--light" style="position:absolute;left:18px;top:18px;font-size:14px">veltaro</div>
  </section>

  <!-- letterhead -->
  <section class="piece letterhead">
    <div class="band" style="top:18px;left:0;right:auto;width:22px;height:10px"></div>
    <div class="wordmark" style="position:absolute;left:30px;top:17px;font-size:14px">veltaro</div>
    <div class="bar" style="top:338px;height:3px"></div>
    <p class="small" style="position:absolute;left:0;right:0;top:346px;text-align:center">246 W. Harbor Ave., Suite 2020, Long Beach, CA 90815<br>855.5.VELTARO · veltaro-example.com</p>
    <div class="band" style="bottom:0;height:12px"></div>
  </section>

  <!-- compliment slip -->
  <section class="piece slip">
    <div class="band" style="top:0;left:0;right:auto;width:22px;height:26px"></div>
    <div class="wordmark" style="position:absolute;left:30px;top:6px;font-size:15px">veltaro</div>
    <div class="bar" style="top:96px;height:3px"></div>
    <p class="small" style="position:absolute;left:0;right:0;top:101px;text-align:center">246 W. Harbor Ave., Suite 2020, Long Beach, CA 90815</p>
    <div class="band" style="bottom:0;height:36px"></div>
  </section>

  <!-- envelope -->
  <section class="piece envelope">
    <svg style="position:absolute;left:0;top:0" width="334" height="42" viewBox="0 0 334 42">
      <polygon points="0,0 334,0 334,20 310,42 24,42 0,20" fill="#111"/>
    </svg>
    <div class="wordmark wordmark--light" style="position:absolute;left:0;right:0;top:15px;text-align:center;font-size:12px">veltaro</div>
    <p class="small" style="position:absolute;left:0;right:0;top:132px;text-align:center">veltaro-example.com</p>
  </section>

  <!-- business card, right -->
  <section class="piece card card--right">
    <div style="width:55%;position:relative">
      <div class="wordmark" style="position:absolute;left:8px;top:14px;font-size:12px">veltaro</div>
    </div>
    <div style="width:45%;background:var(--ink);padding:6px 4px">
      <p class="small small--light" style="font-size:4px">Peter Haldane<br>855.5.VELTARO<br>phal@veltaro-example.com<br>veltaro-example.com</p>
    </div>
  </section>

</main>
</body>
</html>
```